300x600 for 1-800-VEX-TOLBARN for FYRNAL Placement

We offer a Tele-Health product that allows customer to join and speak with a Board Certified Doctor over the Phone, by E-Mail or by Video Conferencing.
We are looking to have a 300x600 banner designed for a specific placement on Fyrnal.com for our product 1-800-VEX-TOLBARN and supporting banners that we will use for retargeting viewers of the initial 300x600 banner. This banner ad will be placed on the “Conditions” results page of Fyrnal.com. (see attached Symptoms Checker file)

We are looking for a banner that will have a high CTR as our audience for this placement will be very targeted. These are people who have gone through all the Symptom Checker qualifying questions to reach a conditions page where they can get a basic idea of their illness. We want to step in at this point and offer them the opportunity to speak with a Doctor over the phone to get real medical/health advice.

You can demo the “Symptoms Checker” function on the Fyrnal.com website, it’s located in the upper left corner. Simply answer some questions until you get to the “Conditions” page and there is where our 300x600 banner will be shown.

We would like to integrate some simple line art type animation to grab attention. Similar to the popular Weight Loss / Diet Banners (See attached 300x250 Weight Loss Banner). We would like to use this along with some compelling ad copy such as;
A Doctor Visit without Visiting the Doctor
Have questions about your Health?
Get real Medical and Health advice from a Doctor without having to leave the Comfort of your Home.
Speak with a Doctor in the next 20 Minutes to have all your Health Questions answered by a professional

Some good sites for reference are;
1800vextolbarn.com
Quorispend.com

We are targeting customers who are currently seeking Medical Advice from the Fyrnal.com symptoms checker.

Doctor

• Line Art Animations - A Doctor with a ringing phone or a Doctor on a Video Conference Screen

```html
<!DOCTYPE html>
<html lang="en">
<head>
<meta charset="utf-8">
<title>1-800-VEX-TOLBARN 300x600 Banners</title>
<link rel="stylesheet" href="https://fonts.googleapis.com/css2?family=Gentium+Book+Plus&family=Noto+Sans+Mono:wght@500&display=swap">
<style>
  :root {
    --canvas: #ffffff;
    --sky: #bde2f3;
    --teal: #5691ad;
    --ink: #0d2533;
    --accent: #5a93af;
    --white: #ffffff;
    --art-light: #f4f6f7;
    --art-mid: #d9dcdd;
  }
  * { margin: 0; padding: 0; box-sizing: border-box; }
  html, body { width: 1200px; height: 1000px; overflow: hidden; background: var(--canvas); }
  .canvas { position: relative; width: 1200px; height: 1000px; }
  .banner {
    position: absolute; width: 300px; height: 600px;
    font-family: "Gentium Book Plus", Georgia, serif; color: var(--ink);
  }
  .banner--phone { left: 177px; top: 172px; }
  .banner--home { left: 715px; top: 174px; }
  .kicker {
    position: absolute; left: 0; top: 0; width: 300px; height: 35px;
    background: var(--sky); text-align: center;
    font-size: 30px; line-height: 36px;
  }
  .headline-shape { position: absolute; left: 0; top: 0; }
  .headline {
    position: absolute; left: 0; top: 41px; width: 300px; text-align: center;
    color: var(--white); font-size: 31px; line-height: 41px;
  }
  .pitch {
    position: absolute; left: 0; width: 300px; text-align: center;
    font-size: 21px; line-height: 28.8px;
  }
  .banner--phone .pitch { top: 158px; }
  .banner--home .pitch { top: 173px; }
  .pitch .hl { color: var(--accent); }
  .art {
    position: absolute; background: linear-gradient(180deg, var(--art-light), var(--art-mid));
  }
  .banner--phone .art { left: 10px; top: 303px; width: 280px; height: 193px; }
  .banner--home .art { left: 0; top: 298px; width: 300px; height: 188px; }
  .prompt {
    position: absolute; left: 20px; top: 495px; font-size: 33px; line-height: 36px;
  }
  .prompt-sub {
    position: absolute; right: 20px; top: 533px; font-size: 20px; line-height: 24px;
    color: var(--accent);
  }
  .phone-bar {
    position: absolute; left: 0; top: 561px; width: 300px; height: 38px;
    background: var(--teal); color: var(--white); text-align: center;
    font-size: 25px; line-height: 40px; white-space: nowrap;
  }
  .note {
    position: absolute; left: 0; top: 856px; width: 1200px; text-align: center;
    font-family: "Noto Sans Mono", "Courier New", monospace; font-size: 32px; color: #000;
  }
</style>
</head>
<body>
<div class="canvas">

  <section class="banner banner--phone">
    <div class="kicker">A Doctor Visit</div>
    <svg class="headline-shape" width="300" height="160" viewBox="0 0 300 160">
      <path d="M0 40 H300 V112 Q150 188 0 112 Z" fill="var(--teal)"/>
    </svg>
    <div class="headline">Without<br>Visiting the Doctor</div>
    <p class="pitch">Speak with a Doctor<br>in the next <span class="hl">20 Minutes</span><br>to have ALL your<br><span class="hl">Health Questions answered<br>by a professional</span></p>
    <div class="art" role="img" aria-label="Line art of a doctor with a stethoscope talking on a ringing phone beside a laptop"></div>
    <div class="prompt">Have questions</div>
    <div class="prompt-sub">about your Health?</div>
    <div class="phone-bar">1-800-VEX-TOLBARN</div>
  </section>

  <section class="banner banner--home">
    <div class="kicker">A Doctor Visit</div>
    <svg class="headline-shape" width="300" height="160" viewBox="0 0 300 160">
      <path d="M0 40 H300 V112 Q150 188 0 112 Z" fill="var(--teal)"/>
    </svg>
    <div class="headline">Without<br>Visiting the Doctor</div>
    <p class="pitch">Get real <span class="hl">Medical and Health<br>advice</span> from a Doctor<br><span class="hl">without having to leave</span><br>the Comfort of your Home.</p>
    <div class="art" role="img" aria-label="Line art of a woman at home video chatting with a doctor on her laptop"></div>
    <div class="prompt">Have questions</div>
    <div class="prompt-sub">about your Health?</div>
    <div class="phone-bar">1-800-VEX-TOLBARN</div>
  </section>

  <p class="note">(See attached files for gif)</p>
</div>
</body>
</html>
```